HARVEST sales brochure

Our company, MedSparrowGrove, has recently undertaken a re-branding overhaul to change our website and corporate materials (color scheme, letterhead, biz cards). In support of this re-branding effort, we need an initial sales brochure designed for our company's services that will reflect the look and feel of the website. The website design, fonts and images are included as attachments for your reference.

The brochure will be distributed primarily via email. The audience will be prospective buyers - generally pharmaceutical companies or smaller biotech companies, either of whom are developing treatments for different diseases.

Attached is a word document which contains the text for the brochure. The powerpoint document titled 'case studies' provides example charts and graphs that can be used.
We would like a final format in a layered PSD (photoshop file).

A modular brochure that would allow us to include one or more case studies based on the sales opportunity would be a plus.
Updates

Attention: The text for the brochure has been updated.

Target Market(s)

Pharmaceutical companies / biotechnology companies

Industry/Entity Type

Pharmaceutical

Requirements
Must have
• Utilize the images we have provided as attachments where possible. And choose from our color palette and fonts.
Nice to have
• Additional graphics that reflect the look and feel per our attachments.

```html
<!DOCTYPE html>
<html lang="en">
<head>
<meta charset="utf-8">
<title>HARVEST brochure – Why We're Here</title>
<link href="https://fonts.googleapis.com/css2?family=Nunito+Sans:wght@400;600;700&display=swap" rel="stylesheet">
<style>
  :root {
    --backdrop: #ececec;
    --paper: #ffffff;
    --slate: #55565b;
    --slate-ghost: #4b4c51;
    --brand-blue: #22acd8;
    --sky: #97d7f4;
    --sun: #fee17f;
    --ink: #4a4a4f;
    --photo-dark: #1f6f86;
    --photo-light: #5fb9d3;
  }
  * { margin: 0; padding: 0; box-sizing: border-box; }
  html, body { width: 1200px; height: 1000px; overflow: hidden; }
  body {
    background: var(--backdrop);
    font-family: "Nunito Sans", Arial, sans-serif;
    position: relative;
  }
  .page {
    position: absolute;
    left: 255px; top: 53px;
    width: 693px; height: 895px;
    background: var(--paper);
    overflow: hidden;
  }
  .masthead {
    position: absolute; left: 0; top: 0;
    width: 693px; height: 90px;
    background: var(--slate);
    overflow: hidden;
  }
  .masthead__ghost {
    position: absolute; left: -8px; top: -18px;
    font-size: 92px; font-weight: 700;
    color: var(--slate-ghost);
    white-space: nowrap; letter-spacing: 1px;
  }
  .masthead__title {
    position: absolute; left: 22px; top: 60px;
    font-size: 31px; font-weight: 600;
    color: #fff; line-height: 1; letter-spacing: -0.5px;
    white-space: nowrap;
  }
  .intro-panel { position: absolute; left: 0; top: 107px; }
  .intro-notch { position: absolute; left: 112px; top: 107px; }
  .intro {
    position: absolute; left: 23px; top: 136px; width: 420px;
    color: #fff;
  }
  .intro__heading { font-size: 19.5px; font-weight: 700; line-height: 1.25; margin-bottom: 6px; }
  .intro__body { font-size: 13.6px; line-height: 1.62; }
  .photo {
    position: absolute; left: 0; top: 378px;
    width: 346px; height: 239px;
    background: linear-gradient(120deg, var(--photo-dark) 0%, var(--photo-light) 45%, var(--photo-dark) 100%);
  }
  .photo-rule {
    position: absolute; left: 0; top: 627px;
    width: 346px; height: 13px; background: var(--sun);
  }
  .challenge { position: absolute; left: 381px; top: 398px; width: 290px; }
  .section-heading {
    color: var(--brand-blue); font-size: 19.5px; font-weight: 700; line-height: 1.1;
    margin-bottom: 10px;
  }
  .section-body { color: var(--ink); font-size: 13.6px; line-height: 1.72; }
  .solution { position: absolute; left: 23px; top: 702px; width: 470px; }
  .footer-bands {
    position: absolute; left: 0; bottom: 0;
    width: 693px; height: 25px; display: flex;
  }
  .footer-bands span { flex: 1; }
  .band--sky { background: var(--sky); }
  .band--sun { background: var(--sun); }
  .band--blue { background: var(--brand-blue); }
  .band--slate { background: var(--slate); }
</style>
</head>
<body>
  <article class="page">
    <header class="masthead">
      <div class="masthead__ghost" aria-hidden="true">WHY WE'RE HERE</div>
      <h1 class="masthead__title">WHY WE’RE HERE</h1>
    </header>

    <svg class="intro-panel" width="693" height="272" viewBox="0 0 693 272" aria-hidden="true">
      <polygon points="0,0 693,0 693,228 410,228 346,271 0,271" fill="var(--brand-blue)"/>
    </svg>
    <svg class="intro-notch" width="28" height="16" viewBox="0 0 28 16" aria-hidden="true">
      <polygon points="0,0 28,0 14,14" fill="var(--paper)"/>
    </svg>

    <section class="intro">
      <h2 class="intro__heading">Every disease community should have a common, accessible patient registry.</h2>
      <p class="intro__body">We’ve heard over and over that creating a shared registry of patients is one of the most valuable things a disease community can do. A registry puts critical information about a disease all in one place. This makes it easier for researchers to study the disease, for patients to learn about front-line treatments and for advocates to speak on behalf of the disease community.</p>
    </section>

    <div class="photo" role="img" aria-label="Blue-toned photo of an older patient smiling while talking with a doctor"></div>
    <div class="photo-rule"></div>

    <section class="challenge">
      <h2 class="section-heading">But registries are<br>hard to maintain.</h2>
      <p class="section-body">Registries are expensive. They need constant upkeep—usually by people with a lot of expertise in disease and data management. Often there are multiple competing registries for one disease, which leads to siloed, dead-end data that nobody can use.</p>
    </section>

    <section class="solution">
      <h2 class="section-heading">MedSparrowGrove is here to fix all of that.</h2>
      <p class="section-body">Our HARVEST platform enables anyone—from individual patients to global research organizations—to collect and share disease data in a way that’s controlled, transparent and centered on patients’ best interests.</p>
    </section>

    <div class="footer-bands" aria-hidden="true">
      <span class="band--sky"></span>
      <span class="band--sun"></span>
      <span class="band--blue"></span>
      <span class="band--slate"></span>
    </div>
  </article>
</body>
</html>
```